Roll-Up Banner für Glückswebsite
Das war eine großartige Zusammenarbeit und unserem sehr knappen Zeitplan extrem entgegenkommend. Das design ist gleichzeitig seriös und trotzdem jung und dynamisch! Perfekt!
Zielgruppe
Die Website, www.freudenpfad.de ermöglicht es jedem Interessierten kostenlos mehr über das eigene Lebensglück, persönliche Stärken, und die eigene Lebenszufriedenheit herauszufinden. Interessierte können online Fragebögen ausfüllen, und erhalten neben einer detaillierten Rückmeldung über die eigenen Möglichkeiten und Stärken, Hinweise dazu, wie Sie an Ihrem eigenen Potenzial arbeiten können. Es handelt sich um ein Kooperationsprojekt der Nordischen Vereinigung für Heitere Seelenkunde der Uni Wendelstein, der HK-Lindau, der Health Academy Marbach und der Uni Falkenried. Zielgruppe für das Banner sind Menschen, die selbst mit Klienten im Kontext der Positiven Psychologie arbeiten oder Menschen, die sich Ihrem eigenen Lebensglück zuwenden wollen.
Aufgabenstellung
Es handelt sich um ein Roll-up Banner in den Maßen 1m Breite und 2 Meter Höhe.
Das Banner sollte so angelegt sein, dass es interessierten Besuchern auf Kongressen vermittelt, was es mit der Seite Freudenpfad.de auf sich hat. Also wissenschaftlich evaluierte kostenfreie online-Fragebögen, die Menschen dabei helfen Ihre eigenen Stärken und Potenziale zu entdecken und dem eigenen Glück näher zu kommen.
Es sollte außerdem das Logo der NVHS darauf zu sehen sein, sowie kleiner die Logos der Forschungskooperationspartner, HK-Lindau, Uni Wendelstein, Uni Falkenried, Health Academy Marbach.
Die Farben sollten zum Logo der NVHS passen.

```html
<!DOCTYPE html>
<html lang="de">
<head>
<meta charset="utf-8">
<title>Freudenpfad Roll-Up</title>
<link href="https://fonts.googleapis.com/css2?family=PT+Sans:wght@400;700&display=swap" rel="stylesheet">
<style>
  :root{
    --stage:#c9ced6;
    --header-bg:#f6f7f9;
    --photo-bg:#dde2e8;
    --navy:#1c3a6b;
    --navy-light:#21466f;
    --navy-dark:#022a5c;
    --green:#86b21f;
    --footer-bg:#e6e8ec;
    --dot-1:#6fc0d2;
    --dot-2:#2a9c90;
    --dot-3:#2a9a5e;
    --white:#ffffff;
    --grey-text:#5a5f66;
  }
  *{box-sizing:border-box;margin:0;padding:0}
  html,body{width:768px;height:1200px;overflow:hidden}
  body{background:var(--stage);font-family:"PT Sans",sans-serif;position:relative}
  .banner{position:absolute;left:78px;top:0;width:612px;height:1200px;display:flex;flex-direction:column;overflow:hidden}

  .banner-header{height:129px;background:var(--header-bg);position:relative}
  .brand{position:absolute;left:54px;top:62px;color:var(--navy)}
  .brand-name{display:flex;align-items:center;gap:7px;font-weight:700;font-size:17px;letter-spacing:2px}
  .brand-dot{width:11px;height:11px;border-radius:50%;background:var(--dot-2)}
  .brand-sub{font-size:7px;line-height:8px;margin-top:3px;max-width:110px}
  .header-url{position:absolute;right:54px;top:88px;font-size:20px;color:var(--navy)}

  .hero{height:285px;background:linear-gradient(90deg,#d4d9df,var(--photo-bg) 60%,#e3e7ec);position:relative}
  .hero-photo{position:absolute;left:0;top:0;width:321px;height:285px;background:linear-gradient(160deg,#cfd5dc 0%,#b9a58f 40%,#d9cbbd 60%,#bcd3e3 100%);opacity:.85}
  .hero-title{position:absolute;left:315px;width:250px;top:78px;text-align:center;font-size:54px;line-height:72px;color:var(--navy)}

  .info{height:634px;background:linear-gradient(120deg,var(--navy-light) 0%,#15386a 45%,var(--navy-dark) 75%);position:relative;color:var(--white)}
  .questions{position:absolute;left:55px;top:40px;font-weight:700;font-size:23px;line-height:31px}
  .answers-lead{position:absolute;left:55px;top:162px;font-weight:700;font-size:23px}
  .steps-line{position:absolute;left:70px;top:252px;width:2px;height:212px;background:#c9d3df}
  .step{position:absolute;left:57px;display:flex;gap:19px}
  .step-dot{width:28px;height:28px;border-radius:50%;border:2px solid #e6edf3;flex:none;margin-top:1px}
  .step-title{font-size:24px;line-height:26px}
  .step-sub{font-size:17px;line-height:20px}
  .step-1{top:238px}.step-1 .step-dot{background:var(--dot-1)}
  .step-2{top:351px}.step-2 .step-dot{background:var(--dot-2)}
  .step-3{top:451px}.step-3 .step-dot{background:var(--dot-3)}
  .tag{position:absolute;left:425px;top:229px;width:190px;height:56px;background:var(--green);color:var(--navy-dark);font-size:14px;line-height:17px;text-align:center;padding-top:10px;transform:rotate(-2deg);transform-origin:left center}

  .rule{height:5px;background:var(--green)}

  .partners{height:147px;background:var(--footer-bg);position:relative;color:var(--navy)}
  .partners-title{position:absolute;left:54px;top:24px;font-size:17px}
  .partner-row{position:absolute;left:54px;right:52px;top:78px;display:flex;justify-content:space-between;align-items:center}
  .partner{display:flex;align-items:center;gap:6px;font-size:11px;color:var(--navy)}
  .partner-mark{width:18px;height:18px;border-radius:50%;background:var(--navy);opacity:.8}
</style>
</head>
<body>
<main class="banner">
  <header class="banner-header">
    <div class="brand">
      <div class="brand-name"><span class="brand-dot"></span>NVHS</div>
      <div class="brand-sub">Nordische Vereinigung für Heitere Seelenkunde</div>
    </div>
    <div class="header-url">www.freudenpfad.de</div>
  </header>

  <section class="hero">
    <div class="hero-photo" role="img" aria-label="Foto eines nachdenklichen jungen Mannes mit lockigem Haar, die Hand am Kinn"></div>
    <h1 class="hero-title" style="font-weight:400">Sind Sie glücklich?</h1>
  </section>

  <section class="info">
    <p class="questions">Haben Sie noch unentdeckte Fähigkeiten?<br>Ist Ihr Leben erfüllt?<br>Oder gibt es da noch mehr?</p>
    <p class="answers-lead">Antworten finden Sie bei Freudenpfad.de:</p>
    <div class="steps-line"></div>
    <div class="step step-1"><span class="step-dot"></span><div><div class="step-title">Online-Fragebogen ausfüllen</div><div class="step-sub">unter www.freudenpfad.de</div></div></div>
    <div class="tag">wissenschaftlich evaluiert<br>kostenfrei | anonym</div>
    <div class="step step-2"><span class="step-dot"></span><div><div class="step-title">Persönliche Rückmeldung erhalten</div><div class="step-sub">über das eigene Potenzial, Stärken und Möglichkeiten</div></div></div>
    <div class="step step-3"><span class="step-dot"></span><div><div class="step-title">Ein noch erfüllteres Leben leben</div><div class="step-sub">mit unseren Ratschlägen</div></div></div>
  </section>

  <div class="rule"></div>

  <footer class="partners">
    <div class="partners-title">Forschungskooperationspartner</div>
    <div class="partner-row">
      <div class="partner"><span class="partner-mark"></span>Uni Wendelstein</div>
      <div class="partner">Health Academy Marbach</div>
      <div class="partner"><span class="partner-mark"></span>HK-Lindau</div>
      <div class="partner"><span class="partner-mark"></span>Uni Falkenried</div>
    </div>
  </footer>
</main>
</body>
</html>
```